Update New Business Card - For Start Up

I need to update my business card, I have our old version for example. I would like to keep to the same colors and theme. We are a threat reporting and case management tool for corporations and educational institutions.

Target Market(s)

Corporate Security and Human Resources, School Administrators and Superintendents.

Industry/Entity Type

Physical Security and Technology.

Contact Information for Business Card

My Name, Founder/CEO, phone number 555-214-6082, Logo, Web...

Colors
0054AA
0677BA
7BADD7
CADEEF
E8F1F8

Requirements
Must have
• Something new and trendy.

```html
<!DOCTYPE html>
<html lang="en">
<head>
<meta charset="utf-8">
<title>Veltrane Business Card</title>
<link rel="stylesheet" href="https://fonts.googleapis.com/css2?family=Montserrat:wght@500;600;700&display=swap">
<style>
  :root {
    --brand-blue: #1d74ba;
    --deep-blue: #0054aa;
    --wave-line: #cadeef;
    --wave-tint: #e8f1f8;
    --paper: #ffffff;
    --ink: #111111;
    --canvas: #f0f0f0;
  }
  * { box-sizing: border-box; margin: 0; padding: 0; }
  html, body {
    width: 1200px; height: 1200px; overflow: hidden;
    background: var(--canvas);
    font-family: "Montserrat", sans-serif;
  }
  .canvas { position: relative; width: 1200px; height: 1200px; }
  .card {
    position: absolute; left: 203px; width: 794px; height: 454px;
    border-radius: 36px; overflow: hidden;
  }
  .card--front { top: 102px; background: var(--brand-blue); }
  .card--back { top: 644px; background: var(--paper); }
  .wave-pattern { position: absolute; inset: 0; }
  .card--front .wave-pattern {
    background: linear-gradient(180deg, #2079bd 0%, var(--brand-blue) 100%);
  }
  .card--back .wave-pattern {
    background: linear-gradient(180deg, var(--paper) 0%, var(--wave-tint) 100%);
  }
  .front-brand {
    position: absolute; inset: 0;
    display: flex; align-items: center; justify-content: center; gap: 20px;
  }
  .front-brand__dot {
    width: 64px; height: 64px; border-radius: 50%; background: var(--paper);
  }
  .front-brand__name {
    color: var(--paper); font-weight: 600; font-size: 54px; letter-spacing: 6px;
  }
  .back-brand {
    position: absolute; left: 33px; top: 8px;
    display: flex; align-items: center; gap: 8px;
  }
  .back-brand__dot {
    width: 52px; height: 52px; border-radius: 50%; background: var(--brand-blue);
  }
  .back-brand__name {
    color: var(--brand-blue); font-weight: 600; font-size: 27px; letter-spacing: 4px;
  }
  .contact-panel { position: absolute; left: 0; top: 65px; width: 470px; height: 325px; }
  .contact-list { position: absolute; left: 39px; top: 0; list-style: none; color: var(--paper); }
  .contact-item {
    position: absolute; left: 0; display: flex; align-items: center; gap: 14px;
    white-space: nowrap;
  }
  .contact-item svg { flex: none; width: 42px; height: 42px; }
  .contact-item--phone { top: 77px; }
  .contact-item--email { top: 142px; }
  .contact-item--web { top: 207px; }
  .contact-text { font-weight: 600; letter-spacing: 3px; }
  .contact-item--phone .contact-text { font-size: 20px; line-height: 27px; }
  .contact-item--email .contact-text { font-size: 20px; }
  .contact-item--web .contact-text { font-size: 18px; margin-top: -12px; margin-left: -6px; }
  .identity {
    position: absolute; left: 500px; width: 230px; top: 172px; text-align: center;
  }
  .identity__name { font-size: 25px; font-weight: 600; color: var(--ink); white-space: nowrap; }
  .identity__rule {
    width: 175px; height: 2px; background: var(--brand-blue); margin: 6px auto 7px;
  }
  .identity__title { font-size: 14px; font-weight: 500; color: var(--ink); white-space: nowrap; }
</style>
</head>
<body>
<main class="canvas">
  <section class="card card--front">
    <div class="wave-pattern" role="img" aria-label="Repeating light blue wavy line pattern"></div>
    <div class="front-brand">
      <span class="front-brand__dot"></span>
      <span class="front-brand__name">VELTRANE</span>
    </div>
  </section>

  <section class="card card--back">
    <div class="wave-pattern" role="img" aria-label="Repeating pale blue wavy line pattern"></div>
    <div class="back-brand">
      <span class="back-brand__dot"></span>
      <span class="back-brand__name">VELTRANE</span>
    </div>

    <svg class="contact-panel" viewBox="0 0 470 325" aria-hidden="true">
      <path d="M0 0 H372 Q381 0 386 8 L469 152 Q473 162 469 172 L386 317 Q381 325 372 325 H0 Z" fill="var(--brand-blue)"/>
    </svg>

    <ul class="contact-list" style="top:65px">
      <li class="contact-item contact-item--phone">
        <svg viewBox="0 0 42 42" aria-hidden="true">
          <circle cx="21" cy="21" r="19.5" fill="none" stroke="#fff" stroke-width="2.2"/>
          <path d="M15 13.5c1-1 2.2-.9 2.8.1l1.5 2.6c.4.8.2 1.6-.5 2.1l-1 .8c.8 2 2.3 3.5 4.2 4.3l.8-1c.5-.7 1.4-.9 2.1-.5l2.6 1.5c1 .6 1.1 1.8.1 2.8-1.6 1.6-4 1.8-6.4.3-2.6-1.6-4.8-3.8-6.3-6.4-1.5-2.5-1.3-4.9.1-6.6z" fill="#fff"/>
        </svg>
        <span class="contact-text">888-899-3799<br>555-214-6082</span>
      </li>
      <li class="contact-item contact-item--email">
        <svg viewBox="0 0 42 42" aria-hidden="true">
          <circle cx="21" cy="21" r="19.5" fill="none" stroke="#fff" stroke-width="2.2"/>
          <rect x="12" y="15" width="18" height="12" fill="#fff"/>
          <path d="M12 15 L21 22 L30 15 M12 27 L18.5 20.5 M30 27 L23.5 20.5" fill="none" stroke="var(--brand-blue)" stroke-width="1.4"/>
        </svg>
        <span class="contact-text">DANA@VELTRANE.COM</span>
      </li>
      <li class="contact-item contact-item--web">
        <svg viewBox="0 0 42 42" aria-hidden="true">
          <circle cx="21" cy="21" r="19.5" fill="none" stroke="#fff" stroke-width="2.2"/>
          <path d="M16 12 L16 28 L19.5 24.5 L22.5 31 L25 30 L22 23.5 L27 23.5 Z" fill="#fff"/>
        </svg>
        <span class="contact-text">WWW.VELTRANE.CO</span>
      </li>
    </ul>

    <div class="identity">
      <p class="identity__name">DANA WHITFIELD</p>
      <div class="identity__rule"></div>
      <p class="identity__title">CHIEF EXECUTIVE OFFICER</p>
    </div>
  </section>
</main>
</body>
</html>
```